I need a business card to give to prospective clients. I am a freelance photographer who photographs most things (except weddings and social stuff) including nature, wildlife and interiors.
I want to look modern and stylish.
I am including a photograph although I am by no means certain that it should be used - what do you think?
More of my images can be seen and downloaded at my Lensora page - just search for Marla Vintree
Target Market(s)
Home owners selling or letting properties, private individuals wanting to buy prints
Industry/Entity Type
Business
Contact Information for Business Card
Marla Vintree Photography
Marla
Fenwick Lodge, Copper Mill Road, Ashbrook, Thornmere, IP31 4QT
Tel: +44 7700 418263. Email: marla@marlavintree.co.uk

```html
<!DOCTYPE html>
<html lang="en">
<head>
<meta charset="utf-8">
<title>Marla Vintree Photography – Business Card</title>
<link href="https://fonts.googleapis.com/css2?family=Marck+Script&display=swap" rel="stylesheet">
<style>
  :root {
    --page-bg: #ffffff;
    --card-white: #ffffff;
    --magenta: #b01a63;
    --leaf-green: #7b9a2c;
    --deep-green: #3f6a2c;
    --damask-light: #9cba3a;
    --damask-dark: #6f8f1f;
    --vine-olive: #7d8c45;
    --photo-light: #b4b653;
    --photo-mid: #8a9a3c;
    --photo-dark: #6f8a35;
    --card-edge: #e2e2e2;
  }
  html, body {
    margin: 0;
    padding: 0;
    width: 1200px;
    height: 1000px;
    overflow: hidden;
    background: var(--page-bg);
  }
  .canvas {
    position: relative;
    width: 1200px;
    height: 1000px;
  }
  .card {
    position: absolute;
    width: 686px;
    height: 408px;
    overflow: hidden;
    box-sizing: border-box;
  }
  .card--front {
    left: 54px;
    top: 42px;
    background: var(--card-white);
    border: 1px solid var(--card-edge);
  }
  .card--back {
    left: 437px;
    top: 518px;
    height: 410px;
  }

  /* front */
  .damask-band {
    position: absolute;
    left: 0;
    top: 0;
    width: 146px;
    height: 100%;
    border-radius: 0 52px 52px 0;
    background: linear-gradient(90deg, var(--damask-dark) 0%, var(--damask-light) 55%, var(--damask-dark) 100%);
  }
  .studio-name {
    position: absolute;
    left: 180px;
    top: 34px;
    margin: 0;
    font-family: "Marck Script", cursive;
    font-weight: 400;
    font-size: 37px;
    color: var(--magenta);
    white-space: nowrap;
  }
  .address {
    position: absolute;
    left: 180px;
    top: 110px;
    margin: 0;
    font-family: "Marck Script", cursive;
    font-style: normal;
    font-size: 23px;
    line-height: 29px;
    color: var(--leaf-green);
    white-space: nowrap;
  }
  .contact {
    position: absolute;
    left: 164px;
    top: 320px;
    margin: 0;
    font-family: "Marck Script", cursive;
    font-size: 23px;
    line-height: 28px;
    color: var(--leaf-green);
    white-space: nowrap;
  }
  .contact a {
    color: inherit;
    text-decoration: none;
  }
  .vine-ornament {
    position: absolute;
    right: 0;
    bottom: 0;
    width: 200px;
    height: 275px;
    border-radius: 120px 0 0 0;
    background: radial-gradient(ellipse at 60% 60%, rgba(125,140,69,0.55) 0%, rgba(125,140,69,0.25) 55%, rgba(125,140,69,0) 80%);
  }

  /* back */
  .flower-photo {
    position: absolute;
    inset: 0;
    background:
      radial-gradient(ellipse 260px 200px at 210px 140px, rgba(205,200,110,0.75), rgba(205,200,110,0) 100%),
      radial-gradient(ellipse 90px 170px at 90px 230px, rgba(200,40,120,0.35), rgba(200,40,120,0) 100%),
      linear-gradient(160deg, var(--photo-light) 0%, var(--photo-mid) 45%, var(--photo-dark) 100%);
  }
  .back-name {
    position: absolute;
    right: 76px;
    bottom: 48px;
    margin: 0;
    font-family: "Marck Script", cursive;
    font-weight: 400;
    font-size: 48px;
    color: var(--deep-green);
    white-space: nowrap;
  }
</style>
</head>
<body>
<main class="canvas">
  <section class="card card--front" aria-label="Business card front">
    <div class="damask-band" role="img" aria-label="Green damask patterned band"></div>
    <h1 class="studio-name">Marla Vintree Photography</h1>
    <address class="address">
      &nbsp;Fenwick Lodge,<br>
      Copper Mill Road,<br>
      Ashbrook, Thornmere,<br>
      IP31 4QT
    </address>
    <p class="contact">
      +44 7700 418263<br>
      <a href="mailto:marla@marlavintree.co.uk">marla@marlavintree.co.uk</a>
    </p>
    <div class="vine-ornament" role="img" aria-label="Olive green swirling vine ornament with small leaves"></div>
  </section>

  <section class="card card--back" aria-label="Business card back">
    <div class="flower-photo" role="img" aria-label="Photograph of a pink wild gladiolus stem against a soft blurred green background"></div>
    <h2 class="back-name">Marla Vintree</h2>
  </section>
</main>
</body>
</html>
```